Tails of Comfort Therapy & Dog Training

I have a dual themed business. I am a nationally recognized dog trainer for NHF (National Hound Federation) and Animal Allies (Pet Therapy). One side of my business card will need to address my pet therapy ministry called "Tails of Comfort Therapy". We visit almost 1,000 people a month bringing emotionally uplifting happy visits for nursing homes, veterans hospitals, hospice care, surgery recovery, school systems, and libraries, etc. In addition to emotionally positive effects, pet therapy also helps with anxiety, mobility, regulating blood pressure, and many more advantages. I've attached 2 graphics that are connected with this ministry; #1 paw print inside ribbon heart, #2 clasping hands sketch. The story behind the clasping hands is that it is an actual picture of my hand holding my mother's hand on her death bed (with a sketch filter used). My mother lived in a different state than I live in, and I had wished she had pet therapy available to her in her last months of life. They would have provided some bright moments to her difficult days. So, I vowed that although I was not able to help my own mother, I could train my own dog to reach out to hundreds of people in the community I live in. I have continued to live up to that vow, and have gone on to become a national trainer for other people who would like to train their pets to do the same thing.SIDE TWO of my business card will be announcing that I am a dog trainer for puppies, basic obedience, pet therapy, ESA (emotional support animals), and service dogs. Additionally, I offer canine body language training, dog agility training, and cognitive training. I have also attached two graphics for this side: #1 NHF logo, #2 Animal Allies Evaluation

Target Market(s)

Industry/Entity Type

Dog Training

Contact Information for Business Card

I'm looking for a designer who is good with color scheme & fonts.
2-sided card
one side for pet therapy
one side for dog training

Logo Text

Tails of ComfortTherapy

Font styles to use
Sans Serif
Decorative

Colors

Designer to choose colors to be used in the design.

Requirements
Must have
• -Contact information: Marla Quince (555) 203-9164
• - Contact information for online: Tails of Comfort Therapy (Facebook, Instagram & Twitter)
• - Graphics for pet therapy: clasping hands
• - Graphics for dog training: NHF Model Neighbor Dog, Animal Allies
• - List of dog training classes I offer: Basic Obedience, NHF Model Neighbor Dog, NHF B.R.I.G.H.T. Pup, Pet Therapy training, ESA (Emotional Support Animal), Service Dog training, Canine Body Language, Dog Agility, Cognitive Training, Dog Trick Training
Nice to have
• appealing graphic for dog training school
• Titles in decorative font (but still easy to read) & detail info in very easy to read font

```html
<!DOCTYPE html>
<html lang="en">
<head>
<meta charset="utf-8">
<title>Tails of Comfort Therapy – Business Card</title>
<link rel="stylesheet" href="https://fonts.googleapis.com/css2?family=Montserrat:wght@400;500;600&family=Roboto:ital,wght@0,400;1,400&display=swap">
<style>
  :root {
    --rust: #8b3f1c;
    --ink: #2e1a10;
    --parchment-light: #f5ece0;
    --parchment-dark: #e6d4bd;
    --paper: #fdfbf8;
    --photo-warm: #d9a679;
    --photo-deep: #a0522d;
    --badge-blue: #1d4f8f;
    --badge-gold: #e9c73a;
    --shadow: rgba(0,0,0,0.14);
  }
  * { margin: 0; padding: 0; box-sizing: border-box; }
  html, body { width: 1200px; height: 900px; overflow: hidden; background: #ffffff; }
  body { position: relative; font-family: "Roboto", Arial, sans-serif; color: var(--ink); }

  .card {
    position: absolute; left: 390px; width: 420px; height: 240px;
    overflow: hidden; box-shadow: 0 4px 10px var(--shadow);
  }
  .card--front { top: 167px; background: radial-gradient(ellipse at 60% 40%, var(--parchment-light), var(--parchment-dark)); }
  .card--back { top: 456px; height: 239px; background: var(--paper); }

  .hands-sketch {
    position: absolute; left: 0; top: 30px; width: 145px; height: 210px;
    background: radial-gradient(ellipse at 50% 45%, #c9a27c 0%, #dcc2a3 45%, rgba(230,212,189,0) 75%);
  }

  .brand-name {
    position: absolute; left: 166px; top: 40px; width: 240px;
    font-family: "Montserrat", sans-serif; font-weight: 500; font-size: 18px;
    color: var(--ink); white-space: nowrap;
  }
  .person-name {
    position: absolute; left: 167px; top: 96px;
    font-family: "Montserrat", sans-serif; font-weight: 600; font-size: 16px;
    letter-spacing: 1.2px; color: var(--ink);
  }
  .person-title { position: absolute; left: 168px; top: 115px; font-size: 11px; }
  .phone { position: absolute; left: 168px; top: 133px; font-size: 16px; letter-spacing: 0.5px; }
  .handle { position: absolute; left: 169px; top: 165px; font-size: 12px; }
  .social { position: absolute; left: 169px; top: 186px; display: flex; gap: 9px; }
  .social span { width: 22px; height: 22px; border-radius: 4px; background: var(--rust); display: block; }
  .band { position: absolute; right: 0; bottom: 0; height: 11px; background: var(--rust); }
  .card--front .band { width: 251px; }
  .card--back .band { width: 205px; }

  .portrait-photo {
    position: absolute; left: 0; top: 0; width: 220px; height: 239px;
    background: linear-gradient(90deg, var(--photo-deep) 0%, var(--photo-warm) 45%, #efe2cf 78%, rgba(253,251,248,0) 100%);
  }

  .heading {
    position: absolute; left: 113px; top: 11px;
    font-family: "Montserrat", sans-serif; font-weight: 600; font-size: 16px; color: var(--rust);
  }
  .class-list { position: absolute; top: 35px; list-style: none; font-size: 11px; line-height: 15px; color: #111; }
  .class-list--left { left: 112px; }
  .class-list--right { left: 259px; }
  .class-list li { display: flex; align-items: center; white-space: nowrap; }
  .class-list svg { width: 9px; height: 9px; margin-right: 5px; fill: var(--rust); flex: none; }
  .class-list small { font-size: 7px; font-style: italic; margin-left: 3px; }

  .bio {
    position: absolute; left: 208px; top: 122px; width: 206px;
    font-style: italic; font-size: 10px; line-height: 12px; color: var(--rust);
  }
  .cert-badge {
    position: absolute; left: 244px; top: 170px; width: 42px; height: 42px; border-radius: 50%;
    background: var(--badge-blue); border: 4px solid var(--badge-gold);
  }
  .partner { position: absolute; left: 308px; top: 171px; display: flex; flex-direction: column; align-items: center; gap: 4px; }
  .partner-dot { width: 24px; height: 24px; border-radius: 50%; background: #c23a5c; }
  .partner-name { font-family: "Montserrat", sans-serif; font-weight: 600; font-size: 12px; color: #3b2a1e; white-space: nowrap; }
</style>
</head>
<body>
  <section class="card card--front" aria-label="Front: pet therapy">
    <div class="hands-sketch" role="img" aria-label="Sketch of two clasped hands"></div>
    <div class="brand-name">Tails of Comfort Therapy</div>
    <div class="person-name">MARLA QUINCE</div>
    <div class="person-title">Director</div>
    <div class="phone">(555) 203-9164</div>
    <div class="handle">Tails of Comfort Therapy</div>
    <div class="social" aria-label="Social media"><span></span><span></span><span></span></div>
    <div class="band"></div>
  </section>

  <section class="card card--back" aria-label="Back: dog training">
    <div class="portrait-photo" role="img" aria-label="Photo of the trainer with her small white dog"></div>
    <h2 class="heading">Dog Training Offered:</h2>
    <svg width="0" height="0" style="position:absolute">
      <symbol id="paw" viewBox="0 0 10 10">
        <circle cx="2" cy="3.5" r="1.2"/><circle cx="4" cy="1.8" r="1.2"/><circle cx="6.2" cy="1.8" r="1.2"/><circle cx="8.2" cy="3.5" r="1.2"/>
        <ellipse cx="5.1" cy="6.8" rx="2.6" ry="2.1"/>
      </symbol>
    </svg>
    <ul class="class-list class-list--left">
      <li><svg><use href="#paw"/></svg>Basic Obedience</li>
      <li><svg><use href="#paw"/></svg>NHF Model Neighbor Dog</li>
      <li><svg><use href="#paw"/></svg>NHF B.R.I.G.H.T. Pup</li>
      <li><svg><use href="#paw"/></svg>Canine Body Language</li>
      <li><svg><use href="#paw"/></svg>Pet Therapy training</li>
    </ul>
    <ul class="class-list class-list--right">
      <li><svg><use href="#paw"/></svg>Service Dog training</li>
      <li><svg><use href="#paw"/></svg>ESA<small>(Emotional Support Animal)</small></li>
      <li><svg><use href="#paw"/></svg>Dog Agility</li>
      <li><svg><use href="#paw"/></svg>Cognitive training</li>
      <li><svg><use href="#paw"/></svg>Dog Trick training</li>
    </ul>
    <p class="bio">Marla Quince is a nationally recognized dog trainer for NHF (National Hound Federation) and Animal Allies (Pet Therapy).</p>
    <div class="cert-badge" role="img" aria-label="Evaluator certification badge"></div>
    <div class="partner"><span class="partner-dot"></span><span class="partner-name">Animal Allies</span></div>
    <div class="band"></div>
  </section>
</body>
</html>
```